CMS Responsive Website
For wedding photographer
Portfolio style website
example website : [url removed, login to view]
[url removed, login to view]
gallery needs to be blog style : [url removed, login to view]
Web Site Quality: an up-to-date and professional web site . In addition, the sites need to have a clean design with easy navigation. web sites must load with all images and links functioning. They must also be compatible with most browsers. We does not favor HTML over Flash-design sites (or visa versa).
Preferably seo friendly.
Winner will be given content/ and logo in word doc which he needs to insert into website for client.
Winner must allow revisons to allow customer satisfaction.
Winner may be paid extra if design exceeds expectations ( up to clients wish)

```html
<!DOCTYPE html>
<html lang="en">
<head>
<meta charset="utf-8">
<title>Ever After Photo — Wedding Photography Sydney</title>
<link href="https://fonts.googleapis.com/css2?family=Open+Sans:ital,wght@0,400;0,600;0,700;1,400&family=Arimo&family=Kreon:wght@300&family=Dancing+Script:wght@500&display=swap" rel="stylesheet">
<style>
  :root{
    --ink:#3d3a38;
    --text:#6b6663;
    --muted:#9a9592;
    --accent:#1ea3dc;
    --red:#d9463a;
    --rule:#dcdcdc;
    --paper:#ffffff;
    --banner:rgba(20,18,16,.85);
  }
  *{margin:0;padding:0;box-sizing:border-box}
  html,body{width:964px;height:1200px;overflow:hidden;background:var(--paper)}
  body{position:relative;font-family:"Open Sans",Arial,sans-serif;color:var(--ink)}
  .abs{position:absolute}

  .brand{left:0;width:964px;top:22px;text-align:center;display:flex;justify-content:center;align-items:center;gap:12px}
  .brand-mark{width:30px;height:30px;border:2px solid var(--ink);border-radius:50%}
  .brand-name{font-family:"Open Sans",Arial,sans-serif;font-size:26px;font-weight:400;color:var(--ink);letter-spacing:3px;text-transform:uppercase}

  .hero{left:0;top:97px;width:964px;height:330px;
    background:radial-gradient(ellipse at 50% 40%,#a98a6b 0%,#6c5440 45%,#2e241b 100%)}
  .couple-banner{left:506px;top:108px;width:330px;height:46px;background:var(--banner);
    color:#fff;font-family:"Open Sans",Arial,sans-serif;font-size:28px;font-weight:700;
    display:flex;align-items:center;justify-content:center;gap:8px}
  .couple-banner .and{font-weight:400}
  .couple-banner .accent{color:var(--accent)}

  .main-nav{left:0;width:964px;top:440px;display:flex;justify-content:center;gap:26px;font-size:11.5px;text-transform:uppercase}
  .main-nav a,.footer-nav a{color:var(--ink);text-decoration:none}
  .main-nav a.active,.footer-nav a.active{color:var(--red)}
  .rule{left:128px;width:708px;height:1px;background:var(--rule)}
  .rule-mark{left:462px;width:40px;height:14px;background:var(--paper)}
  .rule-mark::after{content:"";position:absolute;left:16px;top:3px;width:8px;height:8px;border:1px solid #aaa;transform:rotate(45deg)}

  .tagline{left:0;width:964px;top:503px;text-align:center;font-family:"Arimo",Arial,sans-serif;font-size:14px;letter-spacing:4.5px;text-transform:uppercase;color:var(--ink)}
  .tagline .accent{color:var(--accent)}

  .slider{left:128px;top:558px;width:321px;height:123px;background:linear-gradient(100deg,#3f5a2c 0%,#7a8f4a 45%,#c9b9a0 70%,#566d36 100%)}
  .slider-arrows{right:12px;bottom:6px;color:#fff;font-size:14px;font-weight:700;letter-spacing:4px}
  .post{left:482px;top:564px;width:354px}
  .post p{font-size:10.5px;line-height:16px;color:var(--text);text-align:justify}
  .post hr{border:0;border-top:1px solid var(--rule);margin:7px 0 6px}
  .post .source{font-size:11px;color:var(--accent);line-height:16px}
  .post .date{font-size:11px;color:var(--red);line-height:16px}

  .col-head{top:714px;font-family:"Arimo",Arial,sans-serif;font-size:13px;letter-spacing:2px;text-transform:uppercase;color:var(--ink);text-align:center}
  .vline{width:1px;background:var(--rule);top:717px;height:190px}

  .social{left:128px;top:760px;width:197px;display:grid;grid-template-columns:1fr 1fr;row-gap:22px;text-align:center;font-family:"Open Sans",Arial,sans-serif;font-weight:700;font-size:15px;color:var(--muted)}

  .testimonial{left:336px;width:224px;display:flex;gap:12px}
  .thumb{flex:none;width:44px;height:47px}
  .testimonial blockquote{font-size:9.5px;line-height:12px;font-style:italic;color:var(--text);text-align:justify}
  .testimonial cite{display:block;font-style:normal;font-size:9.5px;color:var(--accent);margin-top:4px}

  .gallery{left:582px;top:754px;display:grid;grid-template-columns:repeat(3,68px);gap:9px 10px}
  .gallery span{display:block;width:68px;height:68px}
  .t1{background:linear-gradient(135deg,#6f8a46,#b8b3a6)}
  .t2{background:linear-gradient(135deg,#d9cfc4,#4c3d34)}
  .t3{background:linear-gradient(135deg,#7d9a57,#c98e6b)}
  .t4{background:linear-gradient(135deg,#3d5a2e,#c7bfb4)}
  .t5{background:linear-gradient(135deg,#efe9e4,#2f2a28)}
  .t6{background:linear-gradient(135deg,#38414d,#c9a48a)}
  .t7{background:linear-gradient(135deg,#8aa06a,#d8c9b8)}
  .t8{background:linear-gradient(135deg,#b7a08d,#5f6b48)}

  .statement{left:128px;width:708px;top:930px;text-align:center;font-family:"Kreon",Georgia,serif;font-weight:300;font-size:22px;line-height:30px;color:var(--ink)}
  .statement .accent{color:var(--accent)}

  .footer-nav{left:0;width:964px;top:1050px;display:flex;justify-content:center;gap:21px;font-size:10.5px;text-transform:uppercase}
  .footer-text{left:150px;width:664px;top:1083px;text-align:center;font-size:9.5px;line-height:13px;color:var(--ink)}
  .copyright{left:128px;top:1175px;font-size:9.5px;color:var(--muted)}
</style>
</head>
<body>
  <header class="abs brand">
    <span class="brand-mark"></span>
    <span class="brand-name">Ever After Photo</span>
  </header>

  <section class="abs hero" role="img" aria-label="Sepia photo of a smiling bride and groom leaning on a wooden railing in a garden"></section>
  <div class="abs couple-banner"><span>Clara</span><span class="and">and</span><span class="accent">Owen</span></div>

  <nav class="abs main-nav">
    <a class="active" href="#">Home</a><a href="#">About</a><a href="#">Weddings</a><a href="#">Blog</a><a href="#">Happy Clents</a><a href="#">Contact</a>
  </nav>
  <div class="abs rule" style="top:474px"></div>
  <div class="abs rule-mark" style="top:467px"></div>

  <h1 class="abs tagline"><span class="accent">Wedding Photography</span> | Sydney</h1>

  <div class="abs slider" role="img" aria-label="Photo of a couple touching foreheads outdoors in warm sunlight">
    <span class="abs slider-arrows">‹ ›</span>
  </div>
  <article class="abs post">
    <p>It is definitely a change being the bride at a wedding and not the photographer, Only 8 more sleeps till I become Mrs. Hale. What have I learnt in preparing to get married? I have learnt that no matter how much you plan something, what will be will be. Tip 1 - Book Venue's &amp; Photographer's ...</p>
    <hr>
    <div class="source">Harlow Photography</div>
    <div class="date">28-02-14, 5.19 Pm</div>
  </article>

  <div class="abs rule" style="top:745px"></div>
  <h2 class="abs col-head" style="left:128px;width:197px">Social Sharing</h2>
  <h2 class="abs col-head" style="left:325px;width:246px">Testimonials</h2>
  <h2 class="abs col-head" style="left:571px;width:265px">Gallery</h2>
  <div class="abs vline" style="left:325px"></div>
  <div class="abs vline" style="left:571px"></div>

  <div class="abs social">
    <span>Friendly</span><span>Chirpy</span><span>Snapbook</span><span>Postly</span>
  </div>

  <div class="abs testimonial" style="top:761px">
    <span class="thumb t7" role="img" aria-label="Photo of the couple"></span>
    <div><blockquote>“If you are looking for a photographer that will capture those special moments over and over, then you are in the right place.”</blockquote><cite>Sam &amp; Olivia</cite></div>
  </div>
  <div class="abs testimonial" style="top:836px">
    <span class="thumb t8" role="img" aria-label="Photo of the couple"></span>
    <div><blockquote>“If you are looking for a photographer that will capture those special moments over and over, then you are in the right place.”</blockquote><cite>Leo Grant &amp; Nadia</cite></div>
  </div>

  <div class="abs gallery" role="img" aria-label="Six wedding photo thumbnails">
    <span class="t1"></span><span class="t2"></span><span class="t3"></span>
    <span class="t4"></span><span class="t5"></span><span class="t6"></span>
  </div>
  <div class="abs rule" style="top:907px"></div>

  <p class="abs statement">Duis eros ligula lacinia quis <span class="accent">euismod in digni.ssim at neq</span>. Aliquam quis conse cte mag. <span class="accent">aliquam sed nibh</span> condi entum ligula consequat egestas.</p>

  <div class="abs rule" style="top:1023px"></div>
  <div class="abs rule-mark" style="top:1016px"></div>

  <footer>
    <nav class="abs footer-nav">
      <a class="active" href="#">Home</a><a href="#">About</a><a href="#">Weddings</a><a href="#">Blog</a><a href="#">Happy Clents</a><a href="#">Gallery</a><a href="#">Testimonials</a><a href="#">Privacy Policy</a><a href="#">Contact</a>
    </nav>
    <p class="abs footer-text">Lorem ipsum dolor sit amet, cons adipiscing elitliquam condimentum. Duis eros ligula lacinia quis euismod in digni.ssim at neq. Aliquam quis conse cte mag. aliquam sed nibh condi entum ligula consequat egestas.</p>
    <p class="abs copyright">Copyright © 2014. Wedding Photography | All Right Reserved</p>
  </footer>
</body>
</html>
```